K&T Fixit and Rebuild general contracting business card design

I already have a logo that I want to use and I need a card that uses that logo and color scheme on the front with the address phone numbers and email and on the back a place for technicians to write in their name and phone number when they hand it out. It will need the License number of License #KTFXTRB318QN.
It should say General Contractor under the company name. The address is
4417 NE 3rd Ave, Ste D246
Vancouver, WA 98612
www.kandtfixitandrebuild.example
office@kandtfixitandrebuild.example
360-555-0182 is the telephone number
360-555-0149 is the fax number

Target Market(s)

Homeowners needing remodel work or repairs in their home.

Industry/Entity Type

Construction

Contact Information for Business Card

Business name, address, phone number, license number, fax number, email, and website on the front and a place to fill in technician's name and number

Font styles to use
Serif

Requirements
Must have
• Business name, address, phone number, license number, fax number, email, and website on the front and a place to fill in technician's name and number
Nice to have
• I uploaded an example of a front that is good.
Should not have
• Froo froo or extra embellishments.

```html
<!DOCTYPE html>
<html lang="en">
<head>
<meta charset="utf-8">
<title>K&amp;T Fixit and Rebuild — Business Card</title>
<link rel="stylesheet" href="https://fonts.googleapis.com/css2?family=Open+Sans:wght@700&display=swap">
<style>
  :root {
    --page-bg: #8c8f91;
    --wood-mid: #b87a3e;
    --wood-light: #c98d4c;
    --wood-dark: #6e4220;
    --edge-dark: #5a3518;
    --ink: #24170d;
    --copper: #b0694a;
    --white: #ffffff;
    --plank-light: #e4e4e4;
    --plank-mid: #c9c9c9;
    --plank-dark: #9a9a9a;
    --back-panel: #f1f0ef;
  }
  * { margin: 0; padding: 0; box-sizing: border-box; }
  html, body { width: 1200px; height: 929px; overflow: hidden; }
  body {
    background: var(--page-bg);
    font-family: "Open Sans", Arial, sans-serif;
    font-weight: 700;
    position: relative;
  }
  .card { position: absolute; overflow: hidden; }

  /* Front */
  .card-front { left: 268px; top: 58px; width: 660px; height: 376px; }
  .front-wood {
    position: absolute; inset: 0 0 31px 0;
    background: radial-gradient(ellipse at 50% 40%, var(--wood-light), var(--wood-mid) 55%, var(--wood-dark));
  }
  .front-edge { position: absolute; top: 0; bottom: 31px; width: 62px;
    background: linear-gradient(90deg, var(--edge-dark), var(--wood-mid)); }
  .front-edge.left { left: 0; }
  .front-edge.right { right: 0; width: 68px;
    background: linear-gradient(270deg, var(--edge-dark), var(--wood-mid)); }
  .plank-strip { position: absolute; left: 0; right: 0; bottom: 0; height: 31px;
    background: linear-gradient(180deg, var(--plank-light), var(--plank-mid) 60%, var(--plank-dark)); }

  .brand-name { color: var(--copper); line-height: 1.05; text-align: center; }
  .brand-tagline { color: var(--copper); text-align: center; letter-spacing: 1px; text-transform: uppercase; }

  .brand-front { position: absolute; left: 0; right: 0; top: 30px; font-size: 36px; }
  .tagline-front { position: absolute; left: 0; right: 0; top: 118px; font-size: 15px; line-height: 1; }
  .license {
    position: absolute; left: 0; right: 0; top: 160px; text-align: center;
    color: var(--white); font-size: 17px; line-height: 20px;
  }
  .contact-line {
    position: absolute; left: 136px; white-space: nowrap;
    color: var(--ink); font-size: 21px; line-height: 24px;
  }
  .contact-icon { position: absolute; left: 89px; width: 18px; height: 18px; }

  /* Back */
  .card-back { left: 263px; top: 489px; width: 674px; height: 388px; background: var(--back-panel); }
  .back-top { position: absolute; left: 0; right: 0; top: 0; height: 40px;
    background: linear-gradient(180deg, var(--plank-light), #d8d8d8); }
  .back-deck { position: absolute; left: 0; right: 0; bottom: 0; height: 133px;
    background: linear-gradient(180deg, var(--plank-mid) 0, var(--plank-light) 10%, #dcdcdc 75%, var(--plank-dark)); }
  .brand-back { position: absolute; left: 62px; top: 112px; width: 232px; font-size: 31px; }
  .tagline-back { position: absolute; left: 62px; top: 196px; width: 232px; font-size: 14px; line-height: 1; }
  .write-in { position: absolute; left: 319px; color: var(--ink); font-size: 25px; line-height: 26px; white-space: nowrap; }
</style>
</head>
<body>

<section class="card card-front" aria-label="Card front">
  <div class="front-wood" role="img" aria-label="Warm brown wood grain board"></div>
  <div class="front-edge left" role="img" aria-label="Cracked tree stump wood edge"></div>
  <div class="front-edge right" role="img" aria-label="Cracked tree stump wood edge"></div>
  <div class="plank-strip" role="img" aria-label="Whitewashed wooden planks"></div>

  <div class="brand-name brand-front">K&amp;T Fixit<br>and Rebuild</div>
  <div class="brand-tagline tagline-front">General Contractor</div>
  <div class="license">License #KTFXTRB318QN</div>

  <svg class="contact-icon" style="top:189px" viewBox="0 0 18 18"><circle cx="9" cy="9" r="9" fill="#fff"/><path d="M5.5 4.5l2 0 1 2.5-1.3 1a6 6 0 0 0 2.8 2.8l1-1.3 2.5 1v2a1 1 0 0 1-1 1A8.5 8.5 0 0 1 4.5 5.5a1 1 0 0 1 1-1z" fill="#9a7a5c"/></svg>
  <svg class="contact-icon" style="top:241px;height:22px" viewBox="0 0 18 22"><path d="M9 1a5 5 0 0 1 5 5c0 3.5-5 9-5 9S4 9.5 4 6a5 5 0 0 1 5-5z" fill="#fff"/><circle cx="9" cy="6" r="1.8" fill="#9a7a5c"/><ellipse cx="9" cy="18" rx="8" ry="2.5" fill="none" stroke="#fff" stroke-width="1.2"/></svg>
  <svg class="contact-icon" style="top:293px" viewBox="0 0 18 18"><circle cx="9" cy="9" r="9" fill="#fff"/><circle cx="9" cy="9" r="5.5" fill="none" stroke="#9a7a5c" stroke-width="1.2"/><path d="M3.5 9h11M9 3.5c-2.5 3-2.5 8 0 11M9 3.5c2.5 3 2.5 8 0 11" fill="none" stroke="#9a7a5c" stroke-width="1"/></svg>
  <svg class="contact-icon" style="top:318px" viewBox="0 0 18 18"><circle cx="9" cy="9" r="9" fill="#fff"/><rect x="4.5" y="6" width="9" height="6.5" fill="#9a7a5c"/><path d="M4.5 6l4.5 3.8L13.5 6" fill="none" stroke="#fff" stroke-width="1"/></svg>

  <span class="contact-line" style="top:186px">360-555-0182</span>
  <span class="contact-line" style="top:212px">360-555-0149</span>
  <span class="contact-line" style="top:239px">4417 NE 3rd Ave, Ste D246</span>
  <span class="contact-line" style="top:265px">Vancouver, WA 98612</span>
  <span class="contact-line" style="top:290px">www.kandtfixitandrebuild.example</span>
  <span class="contact-line" style="top:315px">office@kandtfixitandrebuild.example</span>
</section>

<section class="card card-back" aria-label="Card back">
  <div class="back-top" role="img" aria-label="Whitewashed wooden board"></div>
  <div class="back-deck" role="img" aria-label="Whitewashed wooden plank deck"></div>

  <div class="brand-name brand-back">K&amp;T Fixit<br>and Rebuild</div>
  <div class="brand-tagline tagline-back">General Contractor</div>
  <div class="write-in" style="top:145px">Name: ..............................</div>
  <div class="write-in" style="top:171px">Contact: ...........................</div>
</section>

</body>
</html>
```